Book Cover Design for Carry the HOPE

The title continues with shaped by Heaven's Outline to Pursue Excellence in kindness to neighbours. So HOPE is an acronym for Heaven's Outline Pursuing Excellence. I wrote the book based on what God taught me when my adult daughter passed away. I failed to recognize her gifts of helping people feel valued and loved. Through this discovery, I recognized I had an identity crisis which prevented me from using the gifts God gave me to serve others. The book chapters include: (1) Carry the HOPE, (2) The Author of the HOPE, (3) Beware the HOPE Robber, (4) Defenders of the HOPE, (5) The Purpose of the HOPE, (6) The Manifestation of the HOPE, (7) The Empowerment of the HOPE and (9) The Reward of the HOPE. Please let me know what other information would be helpful in designing my book cover
Target Market(s)
The book is intended for Christians who surrendered just enough to get saved but did not surrender enough for God to transform them to become more Christ-like.
Industry/Entity Type
Christian
Requirements
Must have
- Please ensure each letter in the word HOPE is a different color. Next, ensure the first leet of the words Heaven's Outline and Pursuing Excellence in the make in .... are the same color as the associate letter in HOPE.
For this project, I just want the front cover. I will create a separate paid project for the selected designer to complete the spine and back cover before publishing through Brindlecart.
Nice to have
- Is it possible to make the cover look like a gift you would receive
I also attached potential design ideas for layout. I want to see your creativity come out in the design.
Should not have
- Not applicable

```html
<!DOCTYPE html>
<html lang="en">
<head>
<meta charset="utf-8">
<title>Carry the HOPE — Front Cover</title>
<link rel="stylesheet" href="https://fonts.googleapis.com/css2?family=Bebas+Neue&family=Crimson+Text:ital,wght@1,700&family=Exo+2:ital,wght@0,700;1,800&family=Righteous&family=Ubuntu:wght@500;700&display=swap">
<style>
  :root {
    --peach-light: #fde7c4;
    --peach: #fbc27a;
    --orange: #f6931f;
    --orange-deep: #ee6a10;
    --orange-band: #f28a1c;
    --cream: #fff6de;
    --ink: #0d0d0d;
    --white: #ffffff;
    --teal: #0f6f6c;
    --hope-h: #ff2a8a;
    --hope-o: #d21cc8;
    --hope-p: #8e2fe6;
    --hope-e: #4b2bd6;
    --purple-text: #8a22c9;
    --silhouette: #f07c12;
  }
  * { margin: 0; padding: 0; box-sizing: border-box; }
  html, body { width: 776px; height: 1200px; overflow: hidden; background: var(--white); }
  .cover { position: relative; width: 776px; height: 1200px; overflow: hidden; }

  .cover-art {
    position: absolute; inset: 0 0 250px 0;
    background:
      radial-gradient(ellipse 300px 360px at 530px 620px, rgba(255,250,230,.95), rgba(255,240,200,0) 70%),
      linear-gradient(180deg, var(--peach-light) 0%, var(--peach) 45%, var(--orange) 80%, var(--orange-deep) 100%);
  }
  .hero-figure {
    position: absolute; left: 160px; top: 420px; width: 620px; height: 520px;
    background: linear-gradient(180deg, rgba(246,140,30,0) 0%, rgba(240,124,18,.55) 55%, var(--silhouette) 100%);
    border-radius: 46% 46% 0 0 / 30% 30% 0 0;
  }
  .skyline {
    position: absolute; left: 0; top: 820px; width: 776px; height: 140px;
    background: linear-gradient(180deg, rgba(238,106,16,.35), var(--orange-deep));
  }

  .title { font-size: 16px; font-weight: normal; }
  .title-lead {
    position: absolute; left: 14px; top: 18px; width: 220px;
    font-family: "Exo 2", sans-serif; font-style: italic; font-weight: 800;
    font-size: 52px; line-height: 1.05; color: var(--white);
    -webkit-text-stroke: 2px #9a8f9a; letter-spacing: 1px;
  }
  .title-lead .lead-small {
    display: block; font-size: 52px; margin-left: 70px; margin-top: 10px;
    color: var(--hope-p); -webkit-text-stroke: 2px var(--white);
  }
  .title-main {
    position: absolute; left: 248px; top: 44px;
    font-family: "Righteous", sans-serif; font-size: 170px; line-height: 1;
    letter-spacing: 2px; -webkit-text-stroke: 4px var(--white); paint-order: stroke fill;
    white-space: nowrap;
  }
  .letter-h { color: var(--hope-h); }
  .letter-o { color: var(--hope-o); }
  .letter-p { color: var(--hope-p); }
  .letter-e { color: var(--hope-e); }

  .subtitle {
    position: absolute; left: 0; right: 0; top: 236px; text-align: center;
    font-family: "Crimson Text", serif; font-style: italic; font-weight: 700;
    font-size: 26px; color: var(--teal); white-space: nowrap;
  }
  .subtitle .key { color: var(--purple-text); }

  .byline {
    position: absolute; left: 530px; top: 330px;
    font-family: "Exo 2", sans-serif; font-style: italic; font-weight: 800;
    font-size: 25px; color: var(--teal); line-height: 1.25;
  }
  .byline .byline-name { display: block; margin-left: 28px; color: var(--ink); }

  .theme {
    position: absolute; font-family: "Bebas Neue", sans-serif; color: var(--white);
    line-height: .95; text-align: center; letter-spacing: 1px;
  }
  .theme-left { left: 58px; top: 662px; }
  .theme-left .theme-a { font-size: 56px; display: block; }
  .theme-left .theme-b { font-size: 112px; display: block; }
  .theme-right { left: 520px; top: 618px; color: rgba(255,255,255,.95); }
  .theme-right .theme-a { font-size: 58px; display: block; color: rgba(255,240,225,.85); }
  .theme-right .theme-b { font-size: 82px; display: block; }
  .theme-right .theme-c { font-size: 50px; display: block; }

  .tagline-band {
    position: absolute; left: 0; top: 950px; width: 776px; height: 48px;
    background: linear-gradient(180deg, var(--orange-deep), var(--orange-band));
    display: flex; align-items: center; justify-content: center;
    font-family: "Ubuntu", sans-serif; font-weight: 500; font-size: 19px; color: var(--white);
  }
  .dedication {
    position: absolute; left: 0; top: 1004px; width: 776px; height: 54px;
    background: var(--cream);
    border-top: 6px solid var(--orange-band); border-bottom: 6px solid var(--orange-band);
    display: flex; align-items: center; justify-content: center;
    font-family: "Exo 2", sans-serif; font-weight: 700; font-size: 25px;
    color: var(--purple-text); letter-spacing: 1.5px;
  }
  .author-band {
    position: absolute; left: 0; top: 1068px; width: 776px; height: 108px;
    background: var(--ink);
    display: flex; align-items: center; justify-content: center;
    font-family: "Ubuntu", sans-serif; font-weight: 700; font-size: 50px;
    color: var(--white); letter-spacing: 2px;
  }
  .base-band { position: absolute; left: 0; bottom: 0; width: 776px; height: 24px; background: var(--orange-band); }
</style>
</head>
<body>
<main class="cover">
  <div class="cover-art" role="img" aria-label="Warm peach and orange sky with soft light and drifting butterflies"></div>
  <div class="hero-figure" role="img" aria-label="Orange silhouette of a person standing with arms spread wide"></div>
  <div class="skyline" role="img" aria-label="City skyline silhouette in orange"></div>

  <h1 class="title">
    <span class="title-lead">CARRY<span class="lead-small">THE</span></span>
    <span class="title-main"><span class="letter-h">H</span><span class="letter-o">O</span><span class="letter-p">P</span><span class="letter-e">E</span></span>
  </h1>

  <p class="subtitle">shaped by <span class="letter-h">H</span><span class="key">eaven's</span> <span class="letter-o">O</span><span class="key">utline</span> to <span class="letter-p">P</span><span class="key">ursue</span> <span class="letter-e">E</span><span class="key">xcellence</span> in kindness to neighbours</p>

  <p class="byline">By<span class="byline-name">Author Name</span></p>

  <p class="theme theme-left"><span class="theme-a">MANIFESTATION</span><span class="theme-b">PURPOSE</span></p>
  <p class="theme theme-right"><span class="theme-a">REWARD</span><span class="theme-b">AUTHOR</span><span class="theme-c">EMPOWERMENT</span></p>

  <p class="tagline-band">recoganise the 'HOPES' of people feeling VALUED and LOVED</p>
  <p class="dedication">- Inspired From The Life Of My Daughter -</p>
  <p class="author-band">AUTHOR NAME</p>
  <div class="base-band"></div>
</main>
</body>
</html>
```